Brookvale Systems Yellow rose letterhead

I have a new logo for my company but in its current form it is too large to be used on letterhead or as a email signature. I need to have the designer use elements from the current logo and create something close to the original but more suited for smaller items.
Updates

I just uploaded a copy of our logo that does not have the weathered affect. Thanks

Industry/Entity Type

It Company

Requirements
Must have
• The design must maintain the visual effect of the current logo. It needs to include the yellow rose and the name of the company.
Nice to have
• It would be nice to maintain the stamp theme and incorporate my name, address, phone, email. etc.

```html
<!DOCTYPE html>
<html lang="en">
<head>
<meta charset="utf-8">
<title>Brookvale Systems Letterhead</title>
<link rel="stylesheet" href="https://fonts.googleapis.com/css2?family=Archivo:wght@600;800&display=swap">
<style>
  :root {
    --page-bg: #ffffff;
    --stamp-paper: #f8eba8;
    --stamp-edge: #c9b47a;
    --panel-center: #bab3a3;
    --panel-edge: #c7a966;
    --panel-line: #e8d9a0;
    --brand-teal: #86d6d8;
    --tagline-white: #ffffff;
    --contact-grey: #9c937f;
    --rose-light: #fbe77a;
    --rose-deep: #e0a91e;
  }
  * { margin: 0; padding: 0; box-sizing: border-box; }
  html, body { width: 769px; height: 1200px; overflow: hidden; background: var(--page-bg); }
  .letterhead { position: relative; width: 769px; height: 1200px; }
  .stamp-frame { position: absolute; inset: 0; }
  .panel {
    position: absolute; left: 56px; top: 56px; width: 657px; height: 1086px;
    background: radial-gradient(ellipse at 50% 45%, var(--panel-center) 0%, var(--panel-center) 30%, var(--panel-edge) 100%);
    border: 2px solid var(--panel-line);
  }
  .rose-emblem {
    position: absolute; left: 60px; top: 76px; width: 118px; height: 118px; border-radius: 50%;
    background: radial-gradient(circle at 45% 45%, var(--rose-light) 0%, var(--rose-deep) 85%);
  }
  .brand {
    position: absolute; left: 178px; top: 70px; width: 530px; text-align: center;
  }
  .brand-name {
    font-family: "Archivo", sans-serif; font-weight: 800; font-size: 44px; line-height: 46px;
    color: var(--brand-teal); letter-spacing: 4px; text-transform: uppercase;
  }
  .tagline {
    margin-top: 8px; font-family: "Archivo", sans-serif; font-weight: 800;
    font-size: 27px; line-height: 32px; letter-spacing: 3px; color: var(--tagline-white);
  }
  .mission {
    margin-top: 2px; font-family: "Archivo", sans-serif; font-weight: 600;
    font-size: 20px; line-height: 23px; letter-spacing: 1px; color: var(--tagline-white);
  }
  .contact {
    position: absolute; left: 352px; top: 1020px;
    font-family: "Archivo", sans-serif; font-weight: 800; font-size: 17px; line-height: 21px;
    color: var(--contact-grey); font-style: normal;
  }
</style>
</head>
<body>
<main class="letterhead">
  <svg class="stamp-frame" width="769" height="1200" viewBox="0 0 769 1200">
    <defs>
      <clipPath id="stamp-clip"><rect x="12" y="8" width="745" height="1184"/></clipPath>
    </defs>
    <rect x="12" y="8" width="745" height="1184" fill="var(--stamp-paper)"/>
    <g clip-path="url(#stamp-clip)" fill="var(--page-bg)" stroke="var(--stamp-edge)" stroke-width="2">
      <circle cx="46" cy="8" r="26"/><circle cx="114" cy="8" r="26"/><circle cx="182" cy="8" r="26"/><circle cx="250" cy="8" r="26"/><circle cx="318" cy="8" r="26"/><circle cx="386" cy="8" r="26"/><circle cx="454" cy="8" r="26"/><circle cx="522" cy="8" r="26"/><circle cx="590" cy="8" r="26"/><circle cx="658" cy="8" r="26"/><circle cx="726" cy="8" r="26"/>
      <circle cx="46" cy="1192" r="26"/><circle cx="114" cy="1192" r="26"/><circle cx="182" cy="1192" r="26"/><circle cx="250" cy="1192" r="26"/><circle cx="318" cy="1192" r="26"/><circle cx="386" cy="1192" r="26"/><circle cx="454" cy="1192" r="26"/><circle cx="522" cy="1192" r="26"/><circle cx="590" cy="1192" r="26"/><circle cx="658" cy="1192" r="26"/><circle cx="726" cy="1192" r="26"/>
      <circle cx="12" cy="86" r="26"/><circle cx="12" cy="154" r="26"/><circle cx="12" cy="222" r="26"/><circle cx="12" cy="290" r="26"/><circle cx="12" cy="358" r="26"/><circle cx="12" cy="426" r="26"/><circle cx="12" cy="494" r="26"/><circle cx="12" cy="562" r="26"/><circle cx="12" cy="630" r="26"/><circle cx="12" cy="698" r="26"/><circle cx="12" cy="766" r="26"/><circle cx="12" cy="834" r="26"/><circle cx="12" cy="902" r="26"/><circle cx="12" cy="970" r="26"/><circle cx="12" cy="1038" r="26"/><circle cx="12" cy="1106" r="26"/>
      <circle cx="757" cy="86" r="26"/><circle cx="757" cy="154" r="26"/><circle cx="757" cy="222" r="26"/><circle cx="757" cy="290" r="26"/><circle cx="757" cy="358" r="26"/><circle cx="757" cy="426" r="26"/><circle cx="757" cy="494" r="26"/><circle cx="757" cy="562" r="26"/><circle cx="757" cy="630" r="26"/><circle cx="757" cy="698" r="26"/><circle cx="757" cy="766" r="26"/><circle cx="757" cy="834" r="26"/><circle cx="757" cy="902" r="26"/><circle cx="757" cy="970" r="26"/><circle cx="757" cy="1038" r="26"/><circle cx="757" cy="1106" r="26"/>
    </g>
  </svg>

  <section class="panel"></section>

  <div class="rose-emblem" role="img" aria-label="Illustration of a yellow rose"></div>

  <header class="brand">
    <h1 class="brand-name">Brookvale<br>Systems</h1>
    <p class="tagline">THE SYSTEM BUILDERS</p>
    <p class="mission">Shaping Clear, Reliable and<br>Well-Ordered Business Records</p>
  </header>

  <address class="contact">
    Nora Whitcombe, PhD<br>
    418 Larkspur Avenue, STE 210<br>
    Millbrook, TX 75012<br>
    nora@brookvale-systems.com<br>
    1-800-555-0147
  </address>
</main>
</body>
</html>
```